New company business cards with new company logo

We need a new business card designed as we have a new company logo and are going for a more 'flat design' look. Our company name is Veridanto and we are a global data focused Clinical Research Organisation. We'd ideally like one side with room for the individuals contact details, our full logo and our services - and one side which is quite plain, for example perhaps using the green triangular image attached with just the white 'V' in the center (also attached).

Industry/Entity Type

Business

Requirements
Must have
• Our main colour: #42b5a9
Please make text dark grey: #373737

```html
<!DOCTYPE html>
<html lang="en">
<head>
<meta charset="utf-8">
<title>Veridanto Business Cards</title>
<link href="https://fonts.googleapis.com/css2?family=Lora:wght@400;700&family=Open+Sans:wght@400&display=swap" rel="stylesheet">
<style>
  :root {
    --brand: #42b5a9;
    --brand-faint: rgba(66, 181, 169, 0.13);
    --ink: #373737;
    --rule: #222222;
    --card: #ffffff;
    --stage: #231f20;
  }
  * { margin: 0; padding: 0; box-sizing: border-box; }
  html, body { width: 1024px; height: 1200px; overflow: hidden; }
  body { background: var(--stage); position: relative; font-family: "Lora", Georgia, serif; color: var(--ink); }

  .card { position: absolute; width: 574px; height: 326px; background: var(--card); overflow: hidden; }
  .card--front { left: 39px; top: 86px; z-index: 2; }
  .card--back { left: 432px; top: 367px; z-index: 1; }

  .brand { position: absolute; display: flex; align-items: center; }
  .brand__dot { border-radius: 50%; background: var(--brand); flex: none; }
  .brand__name { font-family: "Open Sans", Arial, sans-serif; font-weight: 400; color: var(--ink); line-height: 1; }

  .card--front .brand { left: 137px; top: 30px; height: 82px; }
  .card--front .brand__dot { width: 82px; height: 82px; margin-right: 14px; }
  .card--front .brand__name { font-size: 40px; }

  .card--back .brand { left: 77px; top: 60px; height: 116px; }
  .card--back .brand__dot { width: 116px; height: 116px; margin-right: 18px; }
  .card--back .brand__name { font-size: 56px; }

  .backdrop-circle { position: absolute; left: 187px; top: 76px; width: 200px; height: 200px; border-radius: 50%; background: var(--brand-faint); }

  .rule { position: absolute; left: 22px; width: 530px; height: 2px; background: var(--rule); }
  .band { position: absolute; left: 22px; width: 530px; top: 296px; height: 9px; background: var(--brand); }
  .card--front .rule { top: 143px; }
  .card--back .rule { top: 236px; }

  .person { position: absolute; left: 25px; top: 200px; }
  .person__name { font-weight: 700; font-size: 18px; color: var(--brand); line-height: 1.15; }
  .person__role { font-weight: 700; font-size: 14px; color: var(--ink); }

  .divider { position: absolute; left: 287px; top: 156px; width: 1px; height: 124px; background: rgba(66, 181, 169, 0.35); }

  .contact { position: absolute; left: 318px; top: 164px; list-style: none; }
  .contact__item { display: flex; align-items: center; height: 37px; font-size: 17px; color: var(--ink); white-space: nowrap; }
  .contact__icon { width: 18px; height: 18px; margin-right: 22px; fill: var(--brand); flex: none; }

  .web { position: absolute; left: 0; width: 100%; top: 252px; text-align: center; font-size: 22px; color: var(--ink); }
  .web__domain { color: var(--brand); }
</style>
</head>
<body>

<section class="card card--front" aria-label="Business card front">
  <div class="backdrop-circle" aria-hidden="true"></div>
  <div class="brand">
    <span class="brand__dot" aria-hidden="true"></span>
    <span class="brand__name">Veridanto</span>
  </div>
  <div class="rule"></div>
  <div class="person">
    <p class="person__name">Firstname lastname</p>
    <p class="person__role">Manger</p>
  </div>
  <div class="divider"></div>
  <ul class="contact">
    <li class="contact__item">
      <svg class="contact__icon" viewBox="0 0 24 24" aria-hidden="true"><path d="M6.6 10.8a15.1 15.1 0 0 0 6.6 6.6l2.2-2.2a1 1 0 0 1 1-.25 11.4 11.4 0 0 0 3.6.57 1 1 0 0 1 1 1V20a1 1 0 0 1-1 1A17 17 0 0 1 3 4a1 1 0 0 1 1-1h3.5a1 1 0 0 1 1 1c0 1.25.2 2.45.57 3.570a1 1 0 0 1-.25 1z"/></svg>
      1300 00 00 00
    </li>
    <li class="contact__item">
      <svg class="contact__icon" viewBox="0 0 24 24" aria-hidden="true"><path d="M2 5h20v2.2l-10 6.3L2 7.2z"/><path d="M2 9.6l10 6.3 10-6.3V19H2z"/></svg>
      info@veridanto.com
    </li>
    <li class="contact__item">
      <svg class="contact__icon" viewBox="0 0 24 24" aria-hidden="true"><path d="M12 2a7 7 0 0 0-7 7c0 5.2 7 13 7 13s7-7.8 7-13a7 7 0 0 0-7-7zm0 9.5A2.5 2.5 0 1 1 12 6.5a2.5 2.5 0 0 1 0 5z"/></svg>
      Office
    </li>
  </ul>
  <div class="band"></div>
</section>

<section class="card card--back" aria-label="Business card back">
  <div class="brand">
    <span class="brand__dot" aria-hidden="true"></span>
    <span class="brand__name">Veridanto</span>
  </div>
  <div class="rule"></div>
  <p class="web">www.<span class="web__domain">brightwellnotes</span>.com</p>
  <div class="band"></div>
</section>

</body>
</html>
```